Vantage Automotive Reconditioning Business Card

We need a professional business card that features our logo, a picture of the employee, and a brief list of our services.
I've attached a logo, and will attach photos at a later date.
The four services that need to be listed are Bumper repair and repainting, road rash repair, clear coat scratch repair, and automotive touch-up.
Target Market(s)
30 - 40 year male general managers of automobile dealerships. They are used to seeing every vendor gimmick under the sun. This brochure needs to impress with its simplicity and honesty.
Industry/Entity Type
Automotive
Look and feel
Each slider illustrates characteristics of the customer's brand and the style your logo design should communicate.

```html
<!DOCTYPE html>
<html lang="en">
<head>
<meta charset="utf-8">
<title>Vantage Automotive Reconditioning – Business Card</title>
<link href="https://fonts.googleapis.com/css2?family=Exo+2:wght@500;800&family=Open+Sans:wght@400;600&display=swap" rel="stylesheet">
<style>
  :root {
    --bg: #e9e9e9;
    --card-light: #f4f4f4;
    --card-mid: #d9d9d9;
    --ink: #262626;
    --ink-soft: #4a4a4a;
    --orange: #ee5a1f;
    --yellow: #f2e21a;
    --yellow-ink: #7d6f0c;
    --photo-light: #c9c9c9;
    --photo-dark: #2c2c2c;
  }
  * { margin: 0; padding: 0; box-sizing: border-box; }
  html, body { width: 1200px; height: 740px; overflow: hidden; }
  body {
    background: var(--bg);
    font-family: "Open Sans", Arial, sans-serif;
    color: var(--ink);
    position: relative;
  }
  .card {
    position: absolute;
    top: 110px;
    width: 300px;
    height: 520px;
    overflow: hidden;
    box-shadow: 0 10px 24px rgba(0,0,0,0.18);
  }
  .card--info {
    left: 270px;
    background: linear-gradient(160deg, var(--card-light) 0%, var(--card-mid) 100%);
  }
  .card--portrait { left: 630px; background: var(--photo-dark); }

  /* Wordmark */
  .brand {
    position: absolute;
    top: 82px;
    left: 34px;
    display: flex;
    align-items: center;
    gap: 10px;
  }
  .brand__dot {
    width: 14px; height: 14px;
    border-radius: 50%;
    background: var(--orange);
    flex: none;
  }
  .brand__name {
    font-family: "Exo 2", Arial, sans-serif;
    font-weight: 800;
    color: var(--ink);
    text-transform: uppercase;
    line-height: 1;
  }
  .brand__main { display: block; font-size: 44px; letter-spacing: 1px; }
  .brand__sub { display: block; font-size: 11.5px; letter-spacing: 0.6px; margin-top: 4px; }

  /* Name bar */
  .name-bar {
    position: absolute;
    top: 196px;
    left: 34px;
    width: 230px;
    height: 28px;
    background: var(--orange);
    display: flex;
    align-items: baseline;
    gap: 10px;
    padding: 4px 10px;
    white-space: nowrap;
  }
  .name-bar__name {
    font-family: "Exo 2", Arial, sans-serif;
    font-weight: 800;
    font-size: 17px;
    color: var(--ink);
    text-transform: uppercase;
  }
  .name-bar__role { font-size: 11px; color: var(--ink); }

  /* Contacts */
  .contacts {
    position: absolute;
    top: 240px;
    left: 52px;
    list-style: none;
    font-size: 12.5px;
    color: var(--ink-soft);
  }
  .contacts li { display: flex; align-items: center; gap: 14px; height: 24px; white-space: nowrap; }
  .contacts svg { width: 14px; height: 14px; flex: none; fill: var(--ink-soft); }
  .address {
    position: absolute;
    top: 326px;
    left: 52px;
    font-size: 12px;
    line-height: 1.3;
    color: var(--ink-soft);
  }

  /* Services */
  .services {
    position: absolute;
    top: 382px;
    left: 34px;
    width: 232px;
    border-top: 2px solid var(--orange);
    padding-top: 10px;
  }
  .services__title {
    font-family: "Exo 2", Arial, sans-serif;
    font-weight: 800;
    font-size: 12px;
    letter-spacing: 0.6px;
    text-transform: uppercase;
    color: var(--ink);
    margin-bottom: 6px;
  }
  .services__list { list-style: none; font-size: 11.5px; color: var(--ink-soft); }
  .services__list li { display: flex; align-items: center; gap: 8px; height: 19px; white-space: nowrap; }
  .services__list li::before {
    content: "";
    width: 6px; height: 6px;
    background: var(--orange);
    flex: none;
  }

  /* Portrait side */
  .portrait {
    position: absolute;
    inset: 0;
    background: radial-gradient(ellipse at 50% 25%, var(--photo-light) 0%, #8f8f8f 45%, var(--photo-dark) 100%);
  }
  .tag {
    position: absolute;
    top: 336px;
    left: 56px;
    width: 188px;
    background: var(--yellow);
    padding: 6px 14px 6px;
    font-family: "Exo 2", Arial, sans-serif;
    box-shadow: 0 2px 6px rgba(0,0,0,0.35);
    white-space: nowrap;
  }
  .tag__name {
    display: block;
    font-weight: 500;
    font-size: 22px;
    letter-spacing: 1px;
    color: var(--ink);
    text-transform: uppercase;
    line-height: 1.1;
  }
  .tag__role {
    display: block;
    font-weight: 500;
    font-size: 14px;
    color: var(--yellow-ink);
    padding-left: 28px;
  }
</style>
</head>
<body>

  <section class="card card--info" aria-label="Card front">
    <div class="brand">
      <span class="brand__dot"></span>
      <p class="brand__name">
        <span class="brand__main">Vantage</span>
        <span class="brand__sub">Automotive Reconditioning</span>
      </p>
    </div>

    <div class="name-bar">
      <span class="name-bar__name">Sam Carter</span>
      <span class="name-bar__role">Mechanic</span>
    </div>

    <ul class="contacts">
      <li>
        <svg viewBox="0 0 14 14" aria-hidden="true"><rect x="3" y="0" width="8" height="14" rx="1.5"/><rect x="4.5" y="2" width="5" height="7" fill="#ddd"/></svg>
        6017 204 8861
      </li>
      <li>
        <svg viewBox="0 0 14 14" aria-hidden="true"><rect x="0" y="2" width="14" height="10" rx="1"/><path d="M1 3 L7 8 L13 3" stroke="#ddd" stroke-width="1.3" fill="none"/></svg>
        samcarter@vantageauto.com
      </li>
      <li>
        <svg viewBox="0 0 14 14" aria-hidden="true"><circle cx="7" cy="7" r="6.5"/><path d="M0.5 7 H13.5 M7 0.5 V13.5 M7 0.5 C3 4 3 10 7 13.5 M7 0.5 C11 4 11 10 7 13.5" stroke="#ddd" stroke-width="1" fill="none"/></svg>
        www.vantageauto.com
      </li>
    </ul>

    <p class="address">Level 2, 88 Harlow Lane, Easton<br>Victoria 3999 Australia</p>

    <div class="services">
      <p class="services__title">Our Services</p>
      <ul class="services__list">
        <li>Bumper repair and repainting</li>
        <li>Road rash repair</li>
        <li>Clear coat scratch repair</li>
        <li>Automotive touch-up</li>
      </ul>
    </div>
  </section>

  <section class="card card--portrait" aria-label="Card back">
    <div class="portrait" role="img" aria-label="Photo of the mechanic in a navy work uniform holding a name plate"></div>
    <div class="tag">
      <span class="tag__name">Sam Carter</span>
      <span class="tag__role">Mechanic</span>
    </div>
  </section>

</body>
</html>
```